File Download Website

We are looking for a design for a file download website. Our objective is to allow users to upload/browse/download files. This means we need 3 different pages.
The upload page should allow users to upload a file, we are looking for creative designs, a file box with a browse button next to it is already out there so the design must bring something new.
The browse page should display a users files/folders.
The download page should allow the user to download a file.
We do not require any code, only design. The designer is given complete freedom over the design, you may go about it however you like. This is a test of creativity, whoever this project goes to will definitely be given more work in the near future.
Example of a well designed file download website: cloudvane.net
Target Market(s)
15-30 year old people
Industry/Entity Type
Work
Look and feel
Each slider illustrates characteristics of the customer's brand and the style your logo design should communicate.

```html
<!DOCTYPE html>
<html lang="en">
<head>
<meta charset="utf-8">
<title>File Manager Layouts</title>
<link rel="stylesheet" href="https://fonts.googleapis.com/css2?family=Questrial&display=swap">
<style>
  :root{
    --page-bg:#f4f4f4;
    --note-grey:#8a8a8a;
    --link-blue:#7cc6ee;
    --panel-white:#f7f6f2;
    --menu-grey:#d9d9d7;
    --ink:#3a3a3a;
    --blue:#29a8f0;
    --green:#35e08a;
    --yellow:#f3e23a;
    --red:#f0505f;
    --orange:#f47a3a;
    --dot:#ffffff;
  }
  *{box-sizing:border-box;margin:0;padding:0}
  html,body{width:1200px;height:1200px;overflow:hidden}
  body{background:var(--page-bg);font-family:"Questrial",sans-serif;color:var(--ink);position:relative}
  .note{position:absolute;left:68px;top:60px}
  .note__label{font-size:22px;color:var(--note-grey);letter-spacing:.5px}
  .note__link{font-size:31px;color:var(--link-blue);margin-top:12px;letter-spacing:1px}

  .screen{position:absolute;top:330px;width:555px;height:350px;overflow:hidden;border-radius:4px;box-shadow:0 10px 30px rgba(0,0,0,.15)}
  .screen--list{left:22px}
  .screen--grid{left:623px}
  .backdrop{position:absolute;inset:0}
  .screen--list .backdrop{background:linear-gradient(180deg,#e9ece9 0%,#f3f2ee 40%,#d8dedb 70%,#4f9c9a 88%,#1d6f73 100%)}
  .screen--grid .backdrop{background:radial-gradient(circle at 85% 85%,#f0357a 0%,rgba(240,53,122,0) 40%),radial-gradient(circle at 90% 20%,#f6e87a 0%,rgba(246,232,122,0) 45%),linear-gradient(135deg,#4f6b3a 0%,#8aa34a 40%,#d8c45a 70%,#e86a5a 100%)}

  /* list view */
  .window{position:absolute;left:18px;top:58px;width:320px;height:222px;background:var(--panel-white);border-radius:3px;box-shadow:0 4px 14px rgba(0,0,0,.12)}
  .crumb{position:absolute;left:10px;top:10px;font-size:7px}
  .crumb b{font-weight:700}
  .col{position:absolute;top:44px;display:flex;flex-direction:column;gap:9px}
  .col--a{left:10px;width:138px}
  .col--b{left:162px;width:118px}
  .col-rule{position:absolute;left:154px;top:40px;width:1px;height:168px;background:#cfcfcf}
  .col-rule--end{left:290px}
  .scroll{position:absolute;left:160px;right:30px;bottom:8px;height:2px;background:#444}
  .pill{height:15px;border:2px solid;border-radius:8px;font-size:6.5px;display:flex;justify-content:space-between;align-items:center;padding:0 7px;background:#fff;white-space:nowrap}
  .pill em{font-style:italic;color:#666}
  .pill--blue{border-color:var(--blue)}
  .pill--active{background:var(--blue);color:#fff}
  .pill--active em{color:#fff}
  .pill--green{border-color:var(--green)}
  .pill--yellow{border-color:var(--yellow)}
  .pill--red{border-color:var(--red);background:var(--red);color:#fff}
  .pill--red em{color:#fff}
  .pill--orange{border-color:var(--orange)}

  .menu{position:absolute;width:112px;background:var(--menu-grey);border-radius:3px;padding:4px 6px 6px;box-shadow:0 3px 10px rgba(0,0,0,.15)}
  .screen--list .menu{left:300px;top:28px}
  .screen--grid .menu{left:428px;top:155px}
  .menu__item{display:flex;align-items:center;gap:7px;height:29px;border-bottom:1px solid #bdbdbb;font-size:8px;color:#555}
  .menu__item svg{width:17px;height:17px;flex:none}
  .menu__settings{text-align:right;font-size:8px;font-weight:700;padding-top:6px;color:#333}

  .caption{position:absolute;left:14px;bottom:48px;font-size:8px;color:#fff}
  .dots{position:absolute;left:14px;bottom:28px;display:flex;gap:7px}
  .dots i{width:6px;height:6px;border-radius:50%;background:var(--dot)}
  .dots i.dark{background:#111}
  .dots i.on{background:var(--blue)}

  /* grid view */
  .browser{position:absolute;left:60px;top:50px;width:340px;height:235px;background:rgba(20,22,20,.7);border-radius:3px}
  .search{position:absolute;left:14px;top:12px;width:120px;height:14px;border:2px solid #eee;border-radius:8px;font-size:6px;color:#ccc;padding:1px 7px}
  .folders{position:absolute;left:14px;top:36px;display:grid;grid-template-columns:repeat(3,100px);row-gap:8px}
  .folder{display:flex;flex-direction:column;align-items:center;text-align:center;color:#ddd}
  .folder svg{width:36px;height:36px}
  .folder__name{font-size:7px;margin-top:3px}
  .folder__date{font-size:5.5px;color:#aaa}
  .view-toggle{position:absolute;right:14px;top:12px;display:flex;gap:4px}
  .view-toggle span{width:13px;height:13px;background:var(--blue);border-radius:1px}
  .view-toggle span+span{background:#fff}
  .add-btn{position:absolute;right:4px;top:2px;width:14px;height:14px}
  .screen--grid .caption{left:232px;bottom:42px}
  .screen--grid .dots{left:266px;bottom:22px}
</style>
</head>
<body>
<svg width="0" height="0" style="position:absolute" aria-hidden="true">
  <symbol id="folder" viewBox="0 0 40 40">
    <rect x="2" y="4" width="36" height="34" rx="5" fill="currentColor"/>
    <path d="M8 14h24v4H8z" fill="#fff"/>
    <path d="M6 18h28v14H6z" fill="#fff" opacity=".85"/>
  </symbol>
  <symbol id="ic-up" viewBox="0 0 20 20"><circle cx="10" cy="10" r="8.5" fill="none" stroke="#222" stroke-width="2"/><path d="M10 15V6M6 10l4-4 4 4" fill="none" stroke="#222" stroke-width="2"/></symbol>
  <symbol id="ic-x" viewBox="0 0 20 20"><circle cx="10" cy="10" r="8.5" fill="none" stroke="#222" stroke-width="2"/><path d="M7 7l6 6M13 7l-6 6" stroke="#222" stroke-width="2"/></symbol>
  <symbol id="ic-plus" viewBox="0 0 20 20"><circle cx="10" cy="10" r="8.5" fill="none" stroke="#222" stroke-width="2"/><path d="M10 6v8M6 10h8" stroke="#222" stroke-width="2"/></symbol>
  <symbol id="ic-down" viewBox="0 0 20 20"><circle cx="10" cy="10" r="8.5" fill="none" stroke="#222" stroke-width="2"/><path d="M10 5v9M6 10l4 4 4-4" fill="none" stroke="#222" stroke-width="2"/></symbol>
</svg>

<header class="note">
  <p class="note__label">please download high resolution example:</p>
  <p class="note__link">https://www.boxvault.io/s/k7m2qfa9wxlrpnt/LAYOUT1.jpg</p>
</header>

<section class="screen screen--list">
  <div class="backdrop" role="img" aria-label="Soft blurred backdrop photo in pale grey fading to teal water"></div>
  <div class="window">
    <p class="crumb">Design Workshop &gt; <b>Final Artwork...</b></p>
    <div class="col col--a">
      <div class="pill pill--blue pill--active">Wireframes<em>folder</em></div>
      <div class="pill pill--blue">Purchased Material<em>folder</em></div>
      <div class="pill pill--blue">Stock Images<em>folder</em></div>
      <div class="pill pill--green">LayeredArt01.LYR<em>image</em></div>
      <div class="pill pill--green">Jpeg01.JPG<em>image</em></div>
      <div class="pill pill--yellow">Text File 01.RTF<em>text</em></div>
      <div class="pill pill--yellow">Text File 02.RTF<em>text</em></div>
    </div>
    <div class="col-rule"></div>
    <div class="col col--b">
      <div class="pill pill--blue">Sub-Folder 01</div>
      <div class="pill pill--blue">Sub-Folder 02</div>
      <div class="pill pill--red">SlideDeck.SLD<em>slides</em></div>
      <div class="pill pill--orange">Vector File.VEC<em>vector</em></div>
    </div>
    <div class="col-rule col-rule--end"></div>
    <div class="scroll"></div>
  </div>
  <nav class="menu">
    <div class="menu__item"><svg><use href="#ic-up"/></svg>Upload file</div>
    <div class="menu__item"><svg><use href="#ic-x"/></svg>Delete folder</div>
    <div class="menu__item"><svg><use href="#ic-plus"/></svg>New folder</div>
    <div class="menu__item"><svg><use href="#ic-down"/></svg>Download file</div>
    <p class="menu__settings">Settings...</p>
  </nav>
  <p class="caption">Design Workshop</p>
  <div class="dots"><i class="dark"></i><i class="on"></i><i></i><i></i><i></i><i></i><i></i><i></i><i></i></div>
</section>

<section class="screen screen--grid">
  <div class="backdrop" role="img" aria-label="Blurred colourful backdrop photo in green, yellow and pink tones"></div>
  <svg class="add-btn" viewBox="0 0 20 20" aria-hidden="true"><circle cx="10" cy="10" r="8.5" fill="none" stroke="#333" stroke-width="1.5"/><path d="M10 6v8M6 10h8" stroke="#333" stroke-width="1.5"/></svg>
  <div class="browser">
    <div class="search">Search</div>
    <div class="view-toggle"><span></span><span></span></div>
    <div class="folders">
      <div class="folder"><svg style="color:var(--blue)"><use href="#folder"/></svg><p class="folder__name">Final Artwork</p><p class="folder__date">Created: 11/04/13</p></div>
      <div class="folder"><svg style="color:var(--green)"><use href="#folder"/></svg><p class="folder__name">Drafts Version 2</p><p class="folder__date">Created: 07/04/13</p></div>
      <div class="folder"><svg style="color:var(--orange)"><use href="#folder"/></svg><p class="folder__name">Example images</p><p class="folder__date">Created: 06/04/13</p></div>
      <div class="folder"><svg style="color:var(--red)"><use href="#folder"/></svg><p class="folder__name">Text (Edited)</p><p class="folder__date">Created: 06/04/13</p></div>
      <div class="folder"><svg style="color:var(--yellow)"><use href="#folder"/></svg><p class="folder__name">Reference Ma...</p><p class="folder__date">Created: 04/04/13</p></div>
      <div></div>
      <div class="folder"><svg style="color:var(--yellow)"><use href="#folder"/></svg><p class="folder__name">Reference im...</p><p class="folder__date">Created: 04/04/13</p></div>
      <div class="folder"><svg style="color:var(--green)"><use href="#folder"/></svg><p class="folder__name">Drafts V1</p><p class="folder__date">Created: 04/04/13</p></div>
    </div>
  </div>
  <nav class="menu">
    <div class="menu__item"><svg><use href="#ic-up"/></svg>Upload file</div>
    <div class="menu__item"><svg><use href="#ic-x"/></svg>Delete folder</div>
    <div class="menu__item"><svg><use href="#ic-plus"/></svg>New folder</div>
    <div class="menu__item"><svg><use href="#ic-down"/></svg>Download file</div>
    <p class="menu__settings">Settings...</p>
  </nav>
  <p class="caption">Design Workshop</p>
  <div class="dots"><i class="dark"></i><i class="dark"></i><i class="dark"></i><i class="dark"></i><i class="on"></i><i></i><i></i><i></i><i></i><i></i><i></i><i></i></div>
</section>
</body>
</html>
```